American cannabis tech company business card design

Thrum.com is seeking a modern, professional, and brand-aligned business card that represents our company and its core values: Mission, Story, Values, and Impact. As an innovative cannabis company, we want a business card that is not only visually appealing but also serves as a representation of who we are and what we stand for.

Project Scope: Design a double-sided business card that integrates our brand identity and core values. Incorporate our key brand elements, ensuring a sleek and contemporary aesthetic. Visually reflect our core values (Mission, Story, Values, Impact) in a way that is engaging yet professional.

Target Market(s)

Vendors, third parties,

Contact Information for Business Card

Contact details (name, title, email, phone, website, etc.)

Font styles to use
Other font styles liked:
• Caslon, Centra

Colors

Designer to choose colors to be used in the design.

Requirements
Must have
• Thrum.com logo and branding A creative yet clean way to integrate our core values (Mission, Story, Values, Impact) Modern typography and a well-structured layout
Nice to have
• forest green, grey, white, black
Should not have
• references to marijuana, leafs, plants, or related product

```html
<!DOCTYPE html>
<html lang="en">
<head>
<meta charset="utf-8">
<title>Thrum.com Business Card</title>
<link rel="stylesheet" href="https://fonts.googleapis.com/css2?family=Poppins:wght@800&family=Outfit:wght@300;400&display=swap">
<style>
  :root {
    --backdrop: #b6b59f;
    --card: #222322;
    --edge: #2e7045;
    --ink: #ffffff;
    --cream: #fdfaf4;
    --muted: #cfe3dc;
    --teal-light: #6fa595;
    --teal-mid: #3f7a66;
    --teal-dark: #1c3a30;
  }
  * { margin: 0; padding: 0; box-sizing: border-box; }
  html, body { width: 764px; height: 1200px; overflow: hidden; }
  body { background: var(--backdrop); position: relative; font-family: "Outfit", sans-serif; }

  .card {
    position: absolute;
    left: 132px;
    width: 500px;
    height: 325px;
    background: var(--card);
    overflow: hidden;
    border-left: 5px solid var(--edge);
    border-right: 5px solid var(--edge);
  }
  .card--front { top: 241px; }
  .card--back { top: 634px; }

  .front__streaks {
    position: absolute;
    left: 0; top: 0;
    width: 490px; height: 190px;
    background:
      linear-gradient(160deg, transparent 0 36%, rgba(111,165,149,0.55) 44%, transparent 52%),
      linear-gradient(165deg, transparent 0 52%, rgba(63,122,102,0.45) 60%, transparent 68%),
      linear-gradient(170deg, rgba(28,58,48,0.6), transparent 70%);
    -webkit-mask-image: linear-gradient(to bottom, #000 60%, transparent 100%);
    mask-image: linear-gradient(to bottom, #000 60%, transparent 100%);
  }
  .front__dots {
    position: absolute;
    left: 0; bottom: 0;
    width: 490px; height: 55px;
    background: linear-gradient(to bottom, transparent, rgba(28,74,60,0.55));
  }

  .front__name {
    position: absolute;
    left: 0; right: 0; top: 56px;
    text-align: center;
    font-family: "Poppins", sans-serif;
    font-weight: 800;
    font-size: 42px;
    line-height: 1;
    color: var(--ink);
    letter-spacing: -0.5px;
  }
  .front__title {
    position: absolute;
    left: 0; right: 0; top: 99px;
    text-align: center;
    font-weight: 400;
    font-size: 16px;
    line-height: 1.2;
    color: var(--ink);
    letter-spacing: 0.3px;
  }

  .contact-list { position: absolute; left: 40px; top: 156px; list-style: none; }
  .contact-list__item {
    display: flex; align-items: center;
    height: 28px;
    color: var(--ink);
    font-weight: 300;
    font-size: 12.5px;
    letter-spacing: 0.3px;
  }
  .contact-list__icon {
    width: 16px; height: 16px;
    margin-right: 14px;
    flex: none;
  }

  .brand-name {
    position: absolute;
    font-family: "Poppins", sans-serif;
    font-weight: 800;
    color: var(--cream);
    line-height: 1;
    letter-spacing: -0.5px;
  }
  .card--front .brand-name { left: 313px; top: 226px; font-size: 38px; }

  .back__glow {
    position: absolute;
    inset: 0;
    background: linear-gradient(to bottom, var(--card) 0 50%, var(--teal-dark) 68%, var(--teal-mid) 85%, var(--teal-light) 100%);
  }
  .card--back .brand-name { left: 0; right: 0; text-align: center; top: 137px; font-size: 50px; }

  .core-values {
    position: absolute;
    left: 0; right: 0; top: 204px;
    display: flex; justify-content: center; gap: 18px;
    list-style: none;
    font-weight: 300;
    font-size: 11px;
    letter-spacing: 2.5px;
    text-transform: uppercase;
    color: var(--muted);
  }
</style>
</head>
<body>

<section class="card card--front">
  <div class="front__streaks" role="img" aria-label="Abstract photo of sweeping teal light streaks"></div>
  <div class="front__dots" role="img" aria-label="Abstract photo of a receding dotted teal surface"></div>

  <h1 class="front__name">Your Name</h1>
  <p class="front__title">Your Title Here</p>

  <ul class="contact-list">
    <li class="contact-list__item">
      <svg class="contact-list__icon" viewBox="0 0 16 16"><circle cx="8" cy="8" r="8" fill="#fff"/><path d="M8 3.6a2.7 2.7 0 0 0-2.7 2.7c0 2 2.7 5 2.7 5s2.7-3 2.7-5A2.7 2.7 0 0 0 8 3.6z" fill="#222322"/><circle cx="8" cy="6.3" r="1" fill="#fff"/></svg>
      your address here
    </li>
    <li class="contact-list__item">
      <svg class="contact-list__icon" viewBox="0 0 16 16"><circle cx="8" cy="8" r="8" fill="#fff"/><path d="M5.2 4.2l1.4-.3.9 2-.9.7c.4 1 1.2 1.8 2.2 2.2l.7-.9 2 .9-.3 1.4c-3.3.2-6.2-2.7-6-6z" fill="#222322"/></svg>
      your contact here
    </li>
    <li class="contact-list__item">
      <svg class="contact-list__icon" viewBox="0 0 16 16"><circle cx="8" cy="8" r="8" fill="#fff"/><rect x="4" y="5.2" width="8" height="5.6" fill="none" stroke="#222322" stroke-width="0.9"/><path d="M4 5.2l4 3.2 4-3.2M4 10.8l3-2.6M12 10.8l-3-2.6" fill="none" stroke="#222322" stroke-width="0.8"/></svg>
      hello@thrum.com
    </li>
    <li class="contact-list__item">
      <svg class="contact-list__icon" viewBox="0 0 16 16"><circle cx="8" cy="8" r="8" fill="#fff"/><g fill="none" stroke="#222322" stroke-width="0.8"><circle cx="8" cy="8" r="4.3"/><ellipse cx="8" cy="8" rx="1.8" ry="4.3"/><path d="M3.7 8h8.6M4.3 5.8h7.4M4.3 10.2h7.4"/></g></svg>
      www.thrum.com
    </li>
  </ul>

  <p class="brand-name">Thrum</p>
</section>

<section class="card card--back">
  <div class="back__glow" role="img" aria-label="Soft photo of a dark surface fading into teal green light"></div>
  <p class="brand-name">Thrum</p>
  <ul class="core-values">
    <li>Mission</li>
    <li>Story</li>
    <li>Values</li>
    <li>Impact</li>
  </ul>
</section>

</body>
</html>
```